Personal Branding - Pilot, Blogger, Speaker

I need a unique card that is remarkable and fits around me and my personal brand. I am an airline captain, blogger, and speaker. I want the card to have some element that is so unique the recipient will have to show someone else how bizarre and unique it is. I also want to stay within the bounds of professionalism. My card will be given out to other airlines to get a better flying job as well as people I want to come to my blog and hire me to speak at their event. I speak on motivation, life goals, learning, and time management. My brand is to inspire others to conquer fear and live remarkably. I want to include the color orange in my design.
Updates

My website is www.tomasrilke.com to get an idea of who I am am what my brand is. I am a motivational speaker, blogger, and entrepreneur. My day job is a captain at an airline. I want to include the following info on my business card. I saw a card that had a crazy mouth on the back and when you hold it in front of your mouth it looks like you're making a silly face. Just one catchy idea I saw and liked. I really want something worth making a remark about when I walk away.Thank You for your designs. Orange, Black, Gray, Red, Tomas K. Rilke Captain Vantor 220 Corvane Airlines 512.638.2094 tomasrilke.com tomasrilke@mailbox.example Speaker, Blogger, Entrepreneur

Project Deadline Extended
Reason: Extension to allow all designers time to complete their projects. Thank you for your designs. Incredible talent.

I've increased the budget of this project because I've shifted my focus slightly. I am including some links here to design ideas that I want to work towards. On the left side of a light gray card I want "tomasrilke.com" in this font. I'm not sure if all black or black and red mix of letters will look best. Maybe the .com will be red https://cdn4.q-img.example/gallery/842/615203/3948-207-58210473619b2e4d71a06c9/KP2_thumb.jpg This website will be the primary focus of the card. To drive traffic to my platform. (the original photo from https://www.gigboard.example/contest/Logo-Design-for-blue-comet-NET-842.html) From the same photo I want the orange streak to come out of the bottom of the "b" in my name and arc back up and through the "o" in .com I want the rocket to be above the website name and flying upwards and to the right of the card. I like the angle of the rocket in the photo, it just needs to be flying the other direction so it passes through the letter "o" I like the colors of gray background, red rocket, orange streak. My contact info in black font will be below this logo and on the lower right of the card: Tomas K. Rilke Captain, VTR-220, Corvane Airlines 512.638.2094 tomasrilke@mailbox.example On the back of the card is just this quote in black on a white background and the words "LIVE YOUR HORIZON" The quote will be in black letters and the "LIVE YOUR HORIZON" will be in red letters. β€œIt’s what you have always wanted to accomplish. Everyone, when they are young, knows what their Personal Legend is. At that point in their lives, everything is clear and everything is possible. They are not afraid to dream, and to yearn for everything they would like to see happen to them in their lives. But, as time passes, a mysterious force begins to convince them that it will be impossible for them to realize their Personal Legend.” ― Marco Viletti, The Lamplighter LIVE YOUR HORIZON. I'll try to submit a sketch somewhere on here. Thank You!!!

Industry/Entity Type

Airlines

```html
<!DOCTYPE html>
<html lang="en">
<head>
<meta charset="utf-8">
<title>Tomas K. Rilke – Business Card</title>
<link rel="stylesheet" href="https://fonts.googleapis.com/css2?family=Cinzel:wght@400&family=Questrial&family=Raleway:wght@300&family=Arimo:wght@400;700&display=swap">
<style>
  :root {
    --backdrop: #dcdcdc;
    --card-white: #fbfbfb;
    --card-gray: #b9b9b9;
    --ink: #1a1a1a;
    --ink-soft: #333333;
    --red: #c8241b;
    --band: #141414;
    --shadow: rgba(0, 0, 0, 0.28);
  }
  * { box-sizing: border-box; margin: 0; padding: 0; }
  html, body {
    width: 1200px;
    height: 900px;
    overflow: hidden;
  }
  body {
    background: radial-gradient(ellipse at 50% 40%, #f4f4f4 0%, var(--backdrop) 75%);
    position: relative;
    font-family: "Arimo", Arial, sans-serif;
  }
  .card {
    position: absolute;
    left: 280px;
    width: 640px;
    height: 366px;
    box-shadow: 0 10px 26px var(--shadow);
    overflow: hidden;
  }

  /* ---------- Back: quote side ---------- */
  .card-back {
    top: 60px;
    background: var(--card-white);
    padding: 48px 40px 0 40px;
  }
  .quote {
    font-family: "Questrial", "Century Gothic", sans-serif;
    font-size: 17px;
    line-height: 1.45;
    color: var(--ink);
    letter-spacing: 0.2px;
  }
  .quote-author { color: var(--red); }
  .tagline {
    margin-top: 34px;
    text-align: right;
    padding-right: 20px;
    font-family: "Raleway", sans-serif;
    font-weight: 300;
    font-size: 30px;
    letter-spacing: 1px;
    color: var(--ink);
  }
  .tagline-accent { color: var(--red); }

  /* ---------- Front: contact side ---------- */
  .card-front {
    top: 474px;
    background: var(--card-gray);
  }
  .identity {
    position: absolute;
    left: 330px;
    top: 84px;
  }
  .identity-name {
    font-family: "Cinzel", serif;
    font-size: 25px;
    font-weight: 400;
    color: var(--ink);
    letter-spacing: 0.5px;
    line-height: 1.1;
  }
  .identity-role {
    font-size: 14px;
    font-weight: 700;
    color: var(--ink-soft);
    line-height: 1.25;
    margin-top: 4px;
  }
  .wordmark {
    position: absolute;
    left: 40px;
    top: 150px;
    display: flex;
    align-items: center;
    gap: 10px;
  }
  .wordmark-dot {
    width: 16px;
    height: 16px;
    border-radius: 50%;
    background: var(--red);
  }
  .wordmark-name {
    font-size: 31px;
    font-weight: 700;
    color: var(--ink);
    letter-spacing: -0.5px;
  }
  .contact-list {
    position: absolute;
    left: 40px;
    top: 224px;
    list-style: none;
  }
  .contact-item {
    display: flex;
    align-items: center;
    gap: 8px;
    font-size: 15px;
    color: var(--ink);
    line-height: 1.65;
  }
  .contact-icon { width: 15px; height: 15px; flex: none; }
  .band {
    position: absolute;
    left: 0;
    right: 0;
    top: 296px;
    height: 26px;
    background: var(--band);
    display: flex;
    align-items: center;
    justify-content: flex-end;
    padding-right: 70px;
  }
  .band-url {
    font-size: 15px;
    font-weight: 700;
    color: var(--red);
    letter-spacing: 0.3px;
  }
  .band-url-light { color: #ffffff; }
</style>
</head>
<body>

  <section class="card card-back" aria-label="Card back">
    <p class="quote">It’s what you have always wanted to accomplish. Everyone, when they are young, knows what their Personal Legend is. At that point in their lives, everything is clear and everything is possible. They are not afraid to dream, and to yearn for everything they would like to see happen to them in their lives. But, as time passes, a mysterious force begins to convince them that it will be impossible for them to realize their Personal Legend.” — <span class="quote-author">Marco Viletti</span>.</p>
    <p class="tagline">LIVE <span class="tagline-accent">YOUR</span> HORIZON</p>
  </section>

  <section class="card card-front" aria-label="Card front">
    <div class="wordmark">
      <span class="wordmark-name">tomasrilke.com</span>
      <span class="wordmark-dot"></span>
    </div>

    <div class="identity">
      <h1 class="identity-name">Tomas K. Rilke</h1>
      <p class="identity-role">Captain, VTR-220<br>Corvane Airlines 512.638.2094</p>
    </div>

    <ul class="contact-list">
      <li class="contact-item">
        <svg class="contact-icon" viewBox="0 0 16 16" aria-hidden="true">
          <rect x="1" y="3" width="14" height="10" rx="1" fill="var(--red)"/>
          <path d="M1.5 3.8 8 9 14.5 3.8" fill="none" stroke="#b9b9b9" stroke-width="1.2"/>
        </svg>
        tomasrilke@mailbox.example
      </li>
      <li class="contact-item">
        <svg class="contact-icon" viewBox="0 0 16 16" aria-hidden="true">
          <circle cx="8" cy="8" r="7" fill="var(--red)"/>
          <g fill="none" stroke="#b9b9b9" stroke-width="0.9">
            <ellipse cx="8" cy="8" rx="3" ry="7"/>
            <line x1="1" y1="8" x2="15" y2="8"/>
            <line x1="2.2" y1="4.5" x2="13.8" y2="4.5"/>
            <line x1="2.2" y1="11.5" x2="13.8" y2="11.5"/>
          </g>
        </svg>
        www.tomasrilke.com
      </li>
    </ul>

    <div class="band">
      <span class="band-url">www.Tomas<span class="band-url-light">Rilke</span>.com</span>
    </div>
  </section>

</body>
</html>
```